Accounting Practice Business Card Design

I have a logo I am happy for you to use in the design of the Business Card.
You can edit and change colours as you please, I am not fixated on it.
I am looking for a modern and clean overall feel for the finished design.

The business is a small accounting practice who thrives on word of mouth referrals and this card will be given to all current and prospect clients.

Industry/Entity Type

Accountant

Contact Information for Business Card

Marcus Vell
Level 5, 8 Ashcombe Ridge Road
FERNMOOR RISE VIC 3187
Phone: 9481 3052
Email: mvell@qrnaccountants.com.au
Web: www.qrnaccountants.com.au

Font styles to use
Serif
Sans Serif

Colors
0555a3
3277b5
85acd3
0393ce
33a6d7
85cae6
00a990
33b8a4
9bcb3c

Requirements
Must have
• "The end to your tax problems begin with us"
• "A referral from you is our greatest compliment"
Nice to have
• Modern clean professional

```html
<!DOCTYPE html>
<html lang="en">
<head>
<meta charset="utf-8">
<title>QRN Accountants – Business Card</title>
<link href="https://fonts.googleapis.com/css2?family=Montserrat:wght@500;700&family=Raleway:wght@400;600&display=swap" rel="stylesheet">
<style>
  :root {
    --bg: #ececec;
    --navy: #1b5592;
    --navy-deep: #174a80;
    --charcoal: #2a2a2a;
    --green: #9bcb3c;
    --sky: #85cae6;
    --white: #f5f6f6;
    --icon-ring: #23415f;
  }
  * { box-sizing: border-box; margin: 0; padding: 0; }
  html, body { width: 1200px; height: 686px; overflow: hidden; background: var(--bg); }
  .stage {
    position: relative; width: 1200px; height: 686px;
    display: flex; align-items: center; justify-content: center; gap: 40px;
  }
  .card {
    position: relative; width: 520px; height: 297px; overflow: hidden;
    box-shadow: 0 10px 28px rgba(0,0,0,.18);
  }

  /* Front */
  .card-front { background: var(--navy); }
  .front-brand {
    position: absolute; left: 0; top: 0; width: 176px; height: 270px;
    background: var(--charcoal);
    display: flex; align-items: flex-end; justify-content: center; padding-bottom: 34px;
  }
  .brand-mark {
    display: flex; align-items: center; gap: 8px;
    font-family: "Montserrat", sans-serif; font-weight: 700;
    color: var(--navy); letter-spacing: 1.5px; font-size: 15px;
  }
  .brand-mark .dot { width: 10px; height: 10px; background: var(--green); }
  .front-details { position: absolute; left: 206px; top: 30px; right: 30px; }
  .person-name {
    font-family: "Raleway", sans-serif; font-weight: 400; font-size: 24px;
    letter-spacing: 3px; text-transform: uppercase; color: var(--sky);
  }
  .person-role {
    font-family: "Montserrat", sans-serif; font-weight: 500; font-size: 9px;
    letter-spacing: 3px; text-transform: uppercase; color: var(--sky); margin-top: 4px;
  }
  .contact-list { list-style: none; margin-top: 22px; }
  .contact-list li {
    display: flex; align-items: center; gap: 14px; margin-bottom: 9px;
    font-family: "Montserrat", sans-serif; font-weight: 700; font-size: 8.5px;
    letter-spacing: 1.6px; text-transform: uppercase; color: #d7e3ef; line-height: 1.5;
  }
  .contact-list svg { flex: none; width: 24px; height: 24px; }
  .front-strip {
    position: absolute; right: 0; top: 120px; width: 12px; height: 150px; background: var(--green);
  }
  .tagline-band {
    position: absolute; left: 0; right: 0; bottom: 0; height: 27px; background: var(--green);
    display: flex; align-items: center; gap: 8px; padding-left: 10px;
    font-family: "Montserrat", sans-serif; font-weight: 700; font-size: 8.5px;
    letter-spacing: 1px; text-transform: uppercase; color: var(--navy-deep);
  }

  /* Back */
  .card-back { background: var(--white); }
  .back-brand {
    position: absolute; left: 0; right: 0; top: 88px; text-align: center;
    font-family: "Montserrat", sans-serif; font-weight: 700; font-size: 38px;
    letter-spacing: 3px; color: var(--navy);
  }
  .back-brand .dot { display: inline-block; width: 20px; height: 20px; background: var(--green); margin-right: 14px; vertical-align: 2px; }
  .referral {
    position: absolute; left: 0; right: 0; top: 158px; text-align: center;
    font-family: "Montserrat", sans-serif; font-weight: 700; font-size: 10px;
    letter-spacing: 2px; text-transform: uppercase; color: var(--navy);
  }
  .back-bar { position: absolute; left: 0; bottom: 0; width: 150px; height: 26px; background: var(--green); }
  .back-edge { position: absolute; right: 0; top: 0; width: 12px; height: 120px; background: var(--green); }
</style>
</head>
<body>
<main class="stage">

  <section class="card card-front" aria-label="Business card front">
    <div class="front-brand">
      <div class="brand-mark"><span class="dot"></span>QRN ACCOUNTANTS</div>
    </div>

    <div class="front-details">
      <h1 class="person-name">Marcus Vell</h1>
      <p class="person-role">Accountant</p>
      <ul class="contact-list">
        <li>
          <svg viewBox="0 0 24 24" aria-hidden="true"><circle cx="12" cy="12" r="12" fill="var(--icon-ring)"/><path d="M8.5 7.5c.6-.6 1.4-.5 1.8.2l.8 1.4c.3.5.2 1.1-.2 1.5l-.6.5c.5 1.2 1.5 2.2 2.7 2.7l.5-.6c.4-.4 1-.5 1.5-.2l1.4.8c.7.4.8 1.2.2 1.8-.9.9-2.2 1.2-3.4.6-2.2-1-3.9-2.7-4.9-4.9-.6-1.2-.3-2.5.6-3.4z" fill="var(--green)"/></svg>
          9481 3052
        </li>
        <li>
          <svg viewBox="0 0 24 24" aria-hidden="true"><circle cx="12" cy="12" r="12" fill="var(--icon-ring)"/><rect x="6.5" y="8" width="11" height="8" fill="none" stroke="#d7e3ef" stroke-width="1.2"/><path d="M6.5 8l5.5 4.5L17.5 8" fill="none" stroke="#d7e3ef" stroke-width="1.2"/></svg>
          Email: mvell@qrnaccountants.com.au
        </li>
        <li>
          <svg viewBox="0 0 24 24" aria-hidden="true"><circle cx="12" cy="12" r="12" fill="var(--icon-ring)"/><g fill="none" stroke="#d7e3ef" stroke-width="1.1"><circle cx="12" cy="12" r="5.5"/><ellipse cx="12" cy="12" rx="2.4" ry="5.5"/><path d="M6.5 12h11M7.3 9.3h9.4M7.3 14.7h9.4"/></g></svg>
          www.qrnaccountants.com.au
        </li>
        <li>
          <svg viewBox="0 0 24 24" aria-hidden="true"><circle cx="12" cy="12" r="12" fill="var(--icon-ring)"/><path d="M12 6.5a4 4 0 0 0-4 4c0 3 4 7 4 7s4-4 4-7a4 4 0 0 0-4-4z" fill="var(--green)"/><circle cx="12" cy="10.5" r="1.5" fill="var(--icon-ring)"/></svg>
          <span>Level 5, 8 Ashcombe Ridge Road<br>Fernmoor Rise VIC 3187</span>
        </li>
      </ul>
    </div>

    <div class="front-strip"></div>
    <div class="tagline-band">
      <svg width="12" height="12" viewBox="0 0 24 24" aria-hidden="true"><path d="M12 2l2.9 6.9 7.1.6-5.4 4.7 1.7 7.3L12 17.6 5.7 21.5l1.7-7.3L2 9.5l7.1-.6z" fill="var(--navy-deep)"/></svg>
      The end to your tax problems begin with us
    </div>
  </section>

  <section class="card card-back" aria-label="Business card back">
    <div class="back-edge"></div>
    <p class="back-brand"><span class="dot"></span>QRN ACCOUNTANTS</p>
    <p class="referral">A referral from you is our greatest compliment</p>
    <div class="back-bar"></div>
  </section>

</main>
</body>
</html>
```